Forget what you know about corporate well

I need a one-page flies used for print, to embedding in a website, all social media platforms and email.

Target Market(s)

Business

Industry/Entity Type

Health And Wellness

Font styles to use
Serif
Script
Other font styles liked:
• I would like the designers opinion on the font

Colors

Designer to choose colors to be used in the design.

Requirements
Must have
• This is the wording:
• Did you know that 75% of healthcare costs are incurred by preventable diseases? Cardiovascular disease, cancer, and diabetes are the three major causes of rising health care plans and are all preventable.
• Owen and his team have spent decades learning how to increase productivity, reduce absenteeism, and increase employee engagement, all leading to lowering healthcare costs. Together, they have developed a system created to target the masses all while addressing individual needs. Their corporate training challenges helps to engrain positive habits through a carefully curated accountability and reward system.
• How it works:
• Step 1 – evaluate the needs of your business;
• Step 2 – set up individualized workshops based on highest needs;
• Step 3 – create a customized corporate training challenge.
• Why Owen?
• Owen excels at motivational speaking. He is an author, a nutritionist and a professional athlete with a master’s degree in clinical nutrition. He is a teacher of corporate wellness at Marbrook College and a health coach. Owen has been featured in national magazines, podcasts, and popular fitness websites. Owen’s own health issues put him on a quest to heal himself and others. With twenty-five years of experience and a passion for wellness, he can provide your company with an unforgettable experience.
Nice to have
• I will not give my opinion, I believe that is an insult to the designer. All of the verbiage is above and I attached a plethora of pictures.
Should not have
• No opinion

```html
<!DOCTYPE html>
<html lang="en">
<head>
<meta charset="utf-8">
<title>Corporate Wellness Flyer</title>
<link rel="stylesheet" href="https://fonts.googleapis.com/css2?family=Gelasio:ital,wght@0,400;0,700;1,400&family=Montserrat:wght@800&display=swap">
<style>
  :root {
    --backdrop: #1e1e1e;
    --lime: #cde64c;
    --lime-text: #c9e33f;
    --charcoal: #333333;
    --ink: #111111;
    --paper: #ffffff;
    --panel: rgba(88, 88, 88, 0.88);
    --photo-dark: #2a241d;
    --photo-warm: #6b5a44;
  }
  * { margin: 0; padding: 0; box-sizing: border-box; }
  html, body {
    width: 1200px; height: 1200px; overflow: hidden;
    background: var(--backdrop);
  }
  .flyer {
    position: absolute; left: 176px; top: 0;
    width: 905px; height: 1281px;
    transform: scale(0.9368); transform-origin: top left;
    overflow: hidden;
    font-family: "Gelasio", Georgia, serif;
    background: var(--charcoal);
  }
  .shapes { position: absolute; inset: 0; }
  .hero-photo {
    position: absolute; left: 0; top: 0; width: 905px; height: 530px;
    background: linear-gradient(160deg, #8a7e6a 0%, var(--photo-warm) 30%, var(--photo-dark) 75%);
  }
  .headline {
    position: absolute; left: 40px; top: 22px;
    font-weight: 700; font-size: 74px; letter-spacing: -1px;
    color: var(--paper); text-shadow: 2px 3px 3px rgba(0,0,0,0.45);
  }
  .headline-sub {
    position: absolute; left: 45px; top: 106px; width: 560px;
    font-style: italic; font-size: 23px; line-height: 24px; letter-spacing: 1.3px;
    color: #1a1a1a;
  }
  .copy {
    position: absolute; font-style: italic; font-size: 17px;
    line-height: 20.7px; letter-spacing: 1px; color: var(--paper);
    text-align: justify; text-align-last: left;
  }
  .copy-stat { left: 36px; top: 207px; width: 516px; }
  .copy-team { left: 335px; top: 467px; width: 508px; }
  .copy-challenge { left: 521px; top: 599px; width: 322px; }
  .portrait {
    position: absolute; left: 53px; top: 541px; width: 205px; height: 268px;
    background: linear-gradient(180deg, #b9a690 0%, #3f5670 45%, #2e4560 70%, rgba(255,255,255,0) 100%);
    border-radius: 90px 90px 0 0;
  }
  .brand {
    position: absolute; left: 208px; top: 735px;
    display: flex; align-items: center; gap: 6px;
    font-weight: 700; font-size: 15px; color: #555555;
  }
  .brand-dot { width: 12px; height: 12px; border-radius: 50%; background: var(--lime-text); }
  .why-title {
    position: absolute; left: 49px; top: 812px;
    font-style: italic; font-size: 50px; letter-spacing: 2px; color: var(--ink);
  }
  .why-body {
    position: absolute; left: 52px; top: 880px; width: 392px;
    font-style: italic; font-size: 16.5px; line-height: 23.7px; letter-spacing: 0.9px;
    color: var(--ink);
  }
  .steps-panel {
    position: absolute; left: 586px; top: 715px; width: 260px; height: 468px;
    background: var(--panel); padding: 30px 0 0 36px;
  }
  .steps-title {
    font-family: "Montserrat", Arial, sans-serif; font-weight: 800;
    font-size: 39px; line-height: 39px; letter-spacing: 2.5px; color: var(--paper);
    margin-bottom: 30px;
  }
  .step { margin-bottom: 20px; }
  .step-label {
    font-family: "Montserrat", Arial, sans-serif; font-weight: 800;
    font-size: 18px; letter-spacing: 1.5px; color: var(--lime-text);
  }
  .step-text {
    font-style: italic; font-size: 19.5px; line-height: 23px; letter-spacing: 1px;
    color: var(--paper);
  }
</style>
</head>
<body>
<div class="flyer">
  <div class="hero-photo" role="img" aria-label="Photo of a speaker presenting to seated employees in an office break room"></div>
  <svg class="shapes" viewBox="0 0 905 1281" width="905" height="1281" aria-hidden="true">
    <polygon points="0,192 620,192 745,0 0,0" fill="#cde64c" opacity="0.93"/>
    <polygon points="650,192 745,0 905,0 905,0 700,150" fill="#e4f28c" opacity="0.25"/>
    <polygon points="0,520 905,325 905,1281 0,1281" fill="#333333"/>
    <polygon points="0,497 116,497 521,761 471,1281 0,1281" fill="#ffffff"/>
    <polygon points="521,761 905,1005 905,1281 471,1281" fill="#000000"/>
  </svg>

  <h1 class="headline">Did you know</h1>
  <p class="headline-sub">that 75% of healthcare costs are incurred by preventable diseases?</p>
  <p class="copy copy-stat">Cardiovascular disease, cancer, and diabetes are the three major causes of rising health care plans and are all preventable.</p>

  <p class="copy copy-team">Owen and his team have spent decades learning how to increase productivity, reduce absenteeism, and increase employee engagement, all leading to lowering healthcare costs. Together, they have developed a system created to target the masses all while addressing individual needs.</p>
  <p class="copy copy-challenge">Their corporate training challenges helps to engrain positive habits through a carefully curated accountability and reward system.</p>

  <div class="portrait" role="img" aria-label="Portrait of Owen smiling with arms crossed, wearing a striped sweater"></div>
  <div class="brand"><span class="brand-dot"></span>Brightpath Wellness</div>

  <h2 class="why-title">Why Owen?</h2>
  <p class="why-body">Owen excels at motivational speaking. He is an author, a nutritionist and a professional athlete with a master’s degree in clinical nutrition. He is a teacher of corporate wellness at Marbrook College and a health coach. Owen has been featured in national magazines, podcasts, and popular fitness websites. Owen’s own health issues put him on a quest to heal himself and others. With twenty-five years of experience and a passion for wellness, he can provide your company with an unforgettable experience.</p>

  <section class="steps-panel">
    <h2 class="steps-title">HOW IT<br>WORKS</h2>
    <div class="step"><div class="step-label">STEP 1</div><div class="step-text">evaluate the needs of your business</div></div>
    <div class="step"><div class="step-label">STEP 2</div><div class="step-text">set up individualized workshops based on highest needs</div></div>
    <div class="step"><div class="step-label">STEP 3</div><div class="step-text">create a customized corporate training challenge</div></div>
  </section>
</div>
</body>
</html>
```